Meditation class design

I need a flyer design for a new meditation class based in Narellan NSW. The information that I want on the flyer is:
'THE QUIET HARBOUR'
Awaken to your purpose. Guiding you to your true divinity.
Allow yourself to invest time for YOU.
Clear the mind with stillness and learn to live in the NOW.
BENEFITS: Balance
Healing the Mind, Body & Spirit
Creates Peace & calmness
Self development
Happiness
Letting go to what is
Clearer mind
Keeps you looking young
Answers
Enriching your life by excepting & embracing who you are
Picture in the whole background of a person sitting down crossed legged looking into the sun with a butterfly around in the distance. Colours to use is shades of purple, white, shades of pink.

I don't need any more designs for my flyer. Can anyone help me to get my file that Pell has created for me.  I have downloaded it but can't see it.

Thank you

REGARDS

MORGAN VELQUIST

• TIME: 10am to 11am
WHERE: Kestrel Fitness Hub, Unit 2
3-5 Wattleby Creek Lane
Narellan NSW
PRICE: $15.00

'ENHANCING THE QUALITY OF YOUR LIFE & THOSE AROUND YOU'

Contact Morgan on 0498 362 105
Email: corvintesa@ripplenet.com
Facebook: Ember Path Wellness

```html
<!DOCTYPE html>
<html lang="en">
<head>
<meta charset="utf-8">
<title>The Quiet Harbour – Meditation Class</title>
<link href="https://fonts.googleapis.com/css2?family=Great+Vibes&family=Dancing+Script:wght@500&family=Parisienne&display=swap" rel="stylesheet">
<style>
  :root {
    --plum-dark: #4a3e5c;
    --plum-band: #55486a;
    --mauve-text: #9a4a78;
    --title-ink: #4b3a5a;
    --header-light: #ffffff;
    --header-blush: #e6d2e2;
    --white: #ffffff;
    --address-bg: #faf8fa;
    --ink: #3a2f44;
  }
  * { box-sizing: border-box; margin: 0; padding: 0; }
  html, body { width: 934px; height: 1200px; overflow: hidden; background: var(--white); }
  .flyer { position: relative; width: 934px; height: 1200px; background: var(--plum-band); overflow: hidden; }

  /* Header */
  .header {
    position: absolute; left: 0; top: 0; width: 934px; height: 162px; overflow: hidden;
    background: linear-gradient(90deg, var(--header-light) 0%, var(--header-light) 25%, #f3e7f0 55%, var(--header-blush) 100%);
  }
  .header__stones {
    position: absolute; left: 0; top: 0; width: 240px; height: 160px;
    background: radial-gradient(ellipse at 40% 55%, #2c2c30 0%, #55555c 35%, #cfd3d8 70%, rgba(255,255,255,0) 100%);
  }
  .header__ornament { position: absolute; width: 100px; height: 48px;
    background: radial-gradient(ellipse at center, rgba(182,108,150,.55), rgba(182,108,150,0) 70%); }
  .header__ornament--top { left: 392px; top: 6px; }
  .header__ornament--bottom { left: 815px; top: 92px; }
  .header__title {
    position: absolute; right: 20px; top: 14px;
    font-family: "Great Vibes", cursive; font-weight: 400; font-size: 52px; line-height: 64px;
    color: var(--title-ink); white-space: nowrap;
  }
  .header__tagline {
    position: absolute; left: 268px; top: 68px;
    font-family: "Parisienne", cursive; font-size: 17px; line-height: 17px; color: var(--ink);
  }

  /* Hero photo */
  .hero {
    position: absolute; left: 0; top: 170px; width: 934px; height: 412px;
    background:
      radial-gradient(circle at 86% 34%, rgba(255,240,190,1) 0%, rgba(246,204,140,.85) 10%, rgba(230,190,170,0) 34%),
      linear-gradient(180deg, #b9a7bb 0%, #d9c3c6 30%, #cfb9b8 41%, #8e9bb0 44%, #7c8ca2 70%, #6e7d94 100%);
  }
  .hero__figure {
    position: absolute; left: 620px; top: 40px; width: 300px; height: 372px;
    background: radial-gradient(ellipse at 50% 60%, rgba(58,50,60,.75) 0%, rgba(58,50,60,.3) 45%, rgba(58,50,60,0) 70%);
  }
  .hero__title {
    position: absolute; left: 178px; top: 170px; white-space: nowrap;
    font-family: "Dancing Script", cursive; font-weight: 500; font-size: 52px; color: var(--white);
    text-shadow: 0 0 6px rgba(80,60,100,.5);
  }
  .hero__subtitle {
    position: absolute; left: 22px; top: 237px; white-space: nowrap;
    font-family: "Parisienne", cursive; font-size: 27px; color: var(--white);
  }

  /* Sunset photo */
  .sunset {
    position: absolute; left: 0; top: 591px; width: 529px; height: 534px;
    background:
      radial-gradient(ellipse at 45% 52%, rgba(255,214,150,1) 0%, rgba(240,150,110,.8) 18%, rgba(200,110,120,0) 45%),
      linear-gradient(180deg, #b98aa0 0%, #e4a28e 35%, #f0b48a 52%, #c67b6e 62%, #5a3b3c 80%, #2e2326 100%);
  }
  .sunset__caption {
    position: absolute; right: 26px; top: 16px; text-align: right; white-space: nowrap;
    font-family: "Parisienne", cursive; font-size: 27px; line-height: 36px; color: var(--white);
  }

  /* Benefits */
  .benefits {
    position: absolute; left: 538px; top: 591px; width: 396px; height: 379px;
    background: var(--white); text-align: center;
  }
  .benefits__heading {
    margin-top: 26px; display: flex; justify-content: center; align-items: center; gap: 14px;
    font-family: "Parisienne", cursive; font-weight: 400; font-size: 26px; color: var(--mauve-text); letter-spacing: 1px;
  }
  .benefits__flourish { width: 72px; height: 30px;
    background: radial-gradient(ellipse at center, rgba(182,108,150,.5), rgba(182,108,150,0) 70%); }
  .benefits__list { list-style: none; margin-top: 10px;
    font-family: "Parisienne", cursive; font-size: 22px; line-height: 30px; color: var(--mauve-text); }

  /* Address */
  .details {
    position: absolute; left: 538px; top: 981px; width: 396px; height: 144px;
    background: var(--address-bg); text-align: center; padding-top: 26px;
    font-family: "Parisienne", cursive; font-size: 18px; line-height: 18px; color: var(--ink);
  }

  /* Footer */
  .footer {
    position: absolute; left: 0; top: 1125px; width: 934px; height: 75px; background: var(--plum-dark);
    font-family: "Parisienne", cursive; font-size: 18px; line-height: 22px; color: var(--white);
  }
  .footer__item { position: absolute; display: flex; align-items: center; gap: 10px; white-space: nowrap; }
  .footer__item svg { width: 20px; height: 20px; flex: none; }
  .footer__item--web { left: 96px; top: 10px; }
  .footer__item--social { left: 96px; top: 43px; }
  .footer__item--email { left: 640px; top: 10px; }
  .footer__item--phone { left: 640px; top: 43px; }
</style>
</head>
<body>
<main class="flyer">
  <header class="header">
    <div class="header__stones" role="img" aria-label="Photo of stacked balancing stones on water"></div>
    <div class="header__ornament header__ornament--top" role="img" aria-label="Decorative floral flourish"></div>
    <div class="header__ornament header__ornament--bottom" role="img" aria-label="Decorative floral flourish"></div>
    <h1 class="header__title">The Quiet Harbour</h1>
    <p class="header__tagline">Awaken to your purpose.<br>Guiding you to your true divinity.<br>Allow yourself to invest time for YOU.<br>Clear the mind with stillness and learn to live in the NOW</p>
  </header>

  <section class="hero" role="img" aria-label="Photo of a woman sitting cross-legged by the sea facing the rising sun, with butterflies">
    <div class="hero__figure"></div>
    <h2 class="hero__title">Meditation Class</h2>
    <p class="hero__subtitle">Enhancing the quality of your life &amp; those around you...</p>
  </section>

  <section class="sunset" role="img" aria-label="Photo of a woman in silhouette sitting on a beach at sunset with arm outstretched">
    <p class="sunset__caption">Enriching your life by excepting<br>&amp; embracing who you are...</p>
  </section>

  <section class="benefits">
    <h3 class="benefits__heading">
      <span class="benefits__flourish" role="img" aria-label="Decorative flourish"></span>
      BENEFITS
      <span class="benefits__flourish" role="img" aria-label="Decorative flourish"></span>
    </h3>
    <ul class="benefits__list">
      <li>Balance</li>
      <li>Healing the Mind, Body &amp; Spirit</li>
      <li>Creates Peace &amp; calmness</li>
      <li>Self development</li>
      <li>Happiness</li>
      <li>Letting go to what is</li>
      <li>Clearer mind</li>
      <li>Keeps you looking young</li>
      <li>Answers</li>
    </ul>
  </section>

  <section class="details">
    <p>Kestrel Fitness Hub,<br>Unit 2, 3-5 Wattleby Creek Lane<br>Narellan NSW<br>10am to 11am<br>$15.00</p>
  </section>

  <footer class="footer">
    <div class="footer__item footer__item--web">
      <svg viewBox="0 0 20 20"><circle cx="10" cy="10" r="8" fill="none" stroke="#fff" stroke-width="1.6"/><ellipse cx="10" cy="10" rx="3.5" ry="8" fill="none" stroke="#fff" stroke-width="1.2"/><line x1="2" y1="10" x2="18" y2="10" stroke="#fff" stroke-width="1.2"/></svg>
      <span>emberpathbymorgan.stillpages.com.au</span>
    </div>
    <div class="footer__item footer__item--social">
      <svg viewBox="0 0 20 20"><circle cx="10" cy="10" r="8" fill="#fff"/></svg>
      <span>Ember Path Wellness</span>
    </div>
    <div class="footer__item footer__item--email">
      <svg viewBox="0 0 20 20"><rect x="2" y="4.5" width="16" height="11" fill="none" stroke="#fff" stroke-width="1.6"/><polyline points="2,4.5 10,11 18,4.5" fill="none" stroke="#fff" stroke-width="1.4"/></svg>
      <span>corvintesa@ripplenet.com</span>
    </div>
    <div class="footer__item footer__item--phone">
      <svg viewBox="0 0 20 20"><circle cx="10" cy="10" r="9" fill="#fff"/><path d="M7 5.5l2 2.2-1.1 1.4c.7 1.3 1.7 2.3 3 3l1.4-1.1 2.2 2-1.2 1.6c-3.4-.4-7.1-4.1-7.5-7.5z" fill="#4a3e5c"/></svg>
      <span>0498 362 105 [Morgan]</span>
    </div>
  </footer>
</main>
</body>
</html>
```